Photography Studio Prep Guide Design Needed

I have a prep guide I send to all parents who book a session - It is outdated and ugly. I want a gorgeous, clean, modern upscale look for the brochure I send.

I already have the text and can provide photos for the final design. I want the cover to be clean and upscale and modern, with a happy feel.

Target Market(s)

My clients for an upscale Newborn Photography Studio

Requirements
Must have
• space for my photos, an upscale clean feel
Nice to have
• I love color, but don't want the brochure to look busy. I love cream, white, pale pink.

```html
<!DOCTYPE html>
<html lang="en">
<head>
<meta charset="utf-8">
<title>Newborn Session Prep Guide</title>
<link rel="stylesheet" href="https://fonts.googleapis.com/css2?family=Cinzel:wght@400;500&family=Open+Sans:wght@400;600&family=Parisienne&display=swap">
<style>
  :root {
    --plum: #5c3a73;
    --plum-light: #6d4c86;
    --wine: #7b1d4f;
    --wine-deep: #6a1540;
    --ink: #3a3a3a;
    --rule: #bdbdbd;
    --paper: #ffffff;
    --gutter: #f1f1f1;
    --photo-a: #8a6a9e;
    --photo-b: #5d6a4c;
  }
  * { margin: 0; padding: 0; box-sizing: border-box; }
  html, body { width: 1200px; height: 791px; overflow: hidden; background: var(--paper); }
  .spread { position: relative; width: 1200px; height: 791px; font-family: "Open Sans", Arial, sans-serif; color: var(--ink); }
  .page-gap { position: absolute; left: 592px; top: 0; width: 18px; height: 791px; background: var(--gutter); }
  .shapes { position: absolute; inset: 0; width: 1200px; height: 791px; }

  /* cover */
  .brand { position: absolute; left: 54px; top: 265px; width: 187px; text-align: center; color: var(--wine); }
  .brand-mark { width: 60px; height: 60px; border-radius: 50%; background: var(--wine); margin: 0 auto 14px; }
  .brand-name { font-family: "Cinzel", Georgia, serif; font-size: 15px; letter-spacing: 2px; line-height: 1.3; }
  .cover-title { position: absolute; left: 54px; top: 464px; width: 187px; border-top: 1px solid var(--rule); border-bottom: 1px solid var(--rule); text-align: center; color: var(--wine); padding: 12px 0 10px; }
  .cover-title .kicker { font-family: "Cinzel", Georgia, serif; font-size: 17px; letter-spacing: 0.5px; }
  .cover-title .script { font-family: "Parisienne", cursive; font-size: 30px; line-height: 1.1; color: var(--plum); }

  /* inside page */
  .section-icon { position: absolute; left: 642px; top: 84px; width: 58px; height: 58px; border-radius: 8px; background: var(--plum); }
  .page-title { position: absolute; left: 718px; top: 76px; font-family: "Cinzel", Georgia, serif; font-weight: 400; font-size: 32px; line-height: 1.08; color: var(--wine); letter-spacing: 1px; }
  .intro { position: absolute; left: 642px; top: 165px; width: 526px; border-top: 1px solid var(--rule); border-bottom: 1px solid var(--rule); padding: 8px 0 11px; }
  .intro h2 { font-weight: 600; font-size: 17px; color: var(--plum); margin-bottom: 4px; }
  .intro p { font-size: 13.5px; line-height: 1.4; }
  .step { position: absolute; top: 262px; }
  .step-one { left: 642px; width: 250px; }
  .step-two { left: 913px; width: 255px; }
  .step h3 { display: flex; align-items: center; gap: 16px; font-family: "Cinzel", Georgia, serif; font-weight: 400; font-size: 21px; color: var(--wine); height: 28px; margin-bottom: 14px; }
  .step h3 svg { width: 26px; height: 28px; flex: none; }
  .step p { font-size: 8.4px; line-height: 1.5; margin-bottom: 6px; }

  .band { position: absolute; top: 779px; height: 12px; }
  .band.wine { background: var(--wine-deep); }
  .band.plum { background: var(--plum); }
</style>
</head>
<body>
<main class="spread">
  <div class="page-gap"></div>

  <svg class="shapes" viewBox="0 0 1146 753" preserveAspectRatio="none" aria-hidden="false">
    <!-- cover collage -->
    <polygon points="272,232 410,155 410,232" fill="var(--plum)"/>
    <polygon points="415,222 498,266 415,314" fill="var(--wine)"/>
    <polygon points="272,240 472,352 348,468 272,525" fill="var(--photo-a)" role="img" aria-label="Photo of a sleeping newborn wrapped in lilac on purple flowers"/>
    <polygon points="352,476 478,362 518,384 518,588" fill="var(--photo-b)" role="img" aria-label="Photo of a newborn in a grey knit outfit asleep on moss"/>
    <polygon points="392,526 515,598 392,668" fill="var(--wine)"/>
    <polygon points="300,606 385,556 385,668" fill="var(--plum-light)"/>
    <!-- inside page collage -->
    <polygon points="645,720 872,458 872,720" fill="var(--photo-a)" role="img" aria-label="Photo of a sleeping newborn in a lilac bonnet on purple flowers"/>
    <polygon points="888,487 1020,555 888,625" fill="var(--wine)"/>
    <polygon points="890,655 958,606 958,695" fill="var(--plum-light)"/>
  </svg>

  <!-- cover -->
  <div class="brand">
    <div class="brand-mark"></div>
    <div class="brand-name">Clara Wynn Photography</div>
  </div>
  <div class="cover-title">
    <div class="kicker">Newborn Session</div>
    <div class="script">Prep Guide</div>
  </div>

  <!-- parent instructions -->
  <div class="section-icon" role="img" aria-label="Baby changing icon"></div>
  <h1 class="page-title">Parent Instructions<br>&amp; Preparations</h1>

  <section class="intro">
    <h2>Congratulations on expecting a baby!</h2>
    <p>Here are my instructions to ensure a successful newborn photography session.<br>Please follow these instructions as closely as possible.</p>
  </section>

  <section class="step step-one">
    <h3><svg viewBox="0 0 26 28"><polygon points="0,0 26,14 0,28" fill="var(--plum)"/></svg>1. Nursing</h3>
    <p>If you are nursing, please avoid eating anything spicy (hot sauce, hot peppers, curry, etc.) that might upset baby's tummy for 24 hours preceding your scheduled session.</p>
    <p>Please if you are breastfeeding do NOT drink caffeine or coffee before your session – I know this is hard but baby will be wired if you have caffeine.</p>
    <p>If you notice baby has a lot of gas after feedings please check with your pediatrician and bring gas drops (TummyEase or other brand) to your session. The most common reason a baby will not settle for a session is gas pressure/discomfort.</p>
  </section>

  <section class="step step-two">
    <h3><svg viewBox="0 0 26 28"><polygon points="0,0 26,14 0,28" fill="var(--plum)"/></svg>2. feeding</h3>
    <p>Feed the baby as much as possible in the 24 hours preceding your session – this will help minimize the amount baby needs to feed during the session, and will help baby sleep as long and as soundly as possible. Feed baby 2-3 hours before your session and not again until you arrive. This feeding is planned in your session time and it's not rushed.</p>
    <p>Please bring an extra bottle of formula or breastmilk to the session if possible – sometimes a small amount of milk in a bottle can quickly soothe a baby back to sleep without requiring a full feeding. I will respect your wishes if you choose not to use a bottle, but please understand we may have to pass on some poses if baby will not settle in position, and I cannot use a bottle to soothe them into the pose.</p>
  </section>

  <div class="band wine" style="left:0;width:497px"></div>
  <div class="band plum" style="left:505px;width:87px"></div>
  <div class="band wine" style="left:610px;width:495px"></div>
  <div class="band plum" style="left:1113px;width:87px"></div>
</main>
</body>
</html>
```